Corvallina
Logo ai and eps files uploaded.
Thanks
please upload the logo ai file or eps
Designers, already looking great. Please include letter head and envelope. Also, the business card is a folded card.
Thanks for participating.
Greta
Logo????
Logo?

```html
<!DOCTYPE html>
<html lang="en">
<head>
<meta charset="utf-8">
<title>Corvallina – Folded Business Card</title>
<link href="https://fonts.googleapis.com/css2?family=Lato:wght@300;400;700&display=swap" rel="stylesheet">
<style>
:root{
  --magenta:#c8157f;
  --magenta-dark:#a70f69;
  --ink:#1c1a1b;
  --taupe:#5b5452;
  --lime:#9ccc2a;
  --paper:#ffffff;
  --mist:#e6e6e8;
  --text:#555;
  --blue:#2a9fd6;
  --pink:#e03fa4;
  --green:#7cc242;
}
*{margin:0;padding:0;box-sizing:border-box}
html,body{width:1200px;height:718px;overflow:hidden;background:var(--paper);font-family:"Lato",sans-serif}
.sheet{position:relative;width:1200px;height:718px}
.card{position:absolute;overflow:hidden}
.front-top{left:43px;top:36px;width:540px;height:326px;border-radius:30px 0 0 0;background:linear-gradient(180deg,#fff 20%,var(--mist) 100%)}
.inside-top{left:605px;top:36px;width:555px;height:326px;border-radius:0 30px 0 0;background:linear-gradient(180deg,#fff 30%,var(--mist) 100%)}
.front-bottom{left:43px;top:368px;width:540px;height:314px;border-radius:0 0 0 30px;background:radial-gradient(circle at 35% 40%,#d9389a 0%,var(--magenta) 55%,var(--magenta-dark) 100%)}
.inside-bottom{left:605px;top:368px;width:555px;height:314px;border-radius:0 0 30px 0;background:linear-gradient(180deg,#fff 30%,var(--mist) 100%)}
.band{position:absolute;left:0;right:0}
.band-ink{background:var(--ink)}
.band-taupe{background:var(--taupe)}
.band-magenta{background:var(--magenta)}
.rule{position:absolute;left:0;right:0;height:4px;background:var(--lime)}
.wordmark{position:absolute;display:flex;align-items:center;gap:14px;font-weight:400;font-size:54px;letter-spacing:1px}
.wordmark .dot{width:22px;height:22px;border-radius:50%}
.wordmark-sub{position:absolute;font-size:22px;letter-spacing:1px}
.web{position:absolute;left:0;right:0;text-align:center;color:#fff;font-size:22px;letter-spacing:9px}
.phone{position:absolute;right:28px;top:20px;color:#fff;font-size:18px}
.person{position:absolute;left:0;right:0;text-align:center}
.person .name{font-size:30px;color:var(--text);font-weight:300}
.person .role{font-size:17px;color:#777;margin-top:4px}
.contact{position:absolute;left:0;right:0;text-align:center;color:#777;font-size:15px;line-height:20px;font-weight:300}
.beads{position:absolute;display:flex;align-items:center;gap:6px}
.bead{border-radius:50%}
.b-pink{background:var(--pink)}.b-green{background:var(--green)}.b-blue{background:var(--blue)}.b-grey{background:#bbb}
</style>
</head>
<body>
<main class="sheet">

  <section class="card front-top" aria-label="Card front">
    <div class="band band-ink" style="top:0;height:30px"></div>
    <div class="band band-magenta" style="top:0;left:0;right:auto;width:70px;height:40px;border-radius:30px 0 40px 0"></div>
    <div class="beads" style="left:100px;top:10px">
      <span class="bead b-pink" style="width:28px;height:28px"></span>
      <span class="bead b-green" style="width:24px;height:24px"></span>
      <span class="bead b-blue" style="width:18px;height:18px"></span>
    </div>
    <div class="wordmark" style="left:70px;top:112px;color:var(--ink)"><span class="dot" style="background:var(--magenta)"></span>Corvallina</div>
    <div class="wordmark-sub" style="left:300px;top:190px;color:var(--magenta)">GRETA MARLOW</div>
    <div class="beads" style="right:40px;top:262px">
      <span class="bead b-blue" style="width:16px;height:16px"></span>
      <span class="bead b-green" style="width:22px;height:22px"></span>
      <span class="bead b-pink" style="width:18px;height:18px"></span>
    </div>
    <div class="rule" style="top:280px"></div>
    <div class="band band-ink" style="top:284px;bottom:0"></div>
    <div class="web" style="top:290px">www.corvallina.com</div>
  </section>

  <section class="card inside-top" aria-label="Card inside, upper panel">
    <div class="band band-taupe" style="top:0;height:54px"></div>
    <div class="band band-magenta" style="top:0;left:0;right:auto;width:70px;height:70px;border-radius:0 0 40px 0"></div>
    <div class="phone">Phone: 555 014 2290</div>
    <div class="beads" style="left:40px;top:40px">
      <span class="bead b-pink" style="width:24px;height:24px"></span>
      <span class="bead b-green" style="width:34px;height:34px"></span>
      <span class="bead b-blue" style="width:26px;height:26px"></span>
    </div>
    <div class="person" style="top:128px"><div class="name">Greta Marlow</div><div class="role">Designer</div></div>
    <div class="rule" style="top:262px;left:40px;border-radius:20px 0 0 0"></div>
    <div class="band band-magenta" style="top:266px;bottom:0;left:0"></div>
    <div class="beads" style="right:60px;top:254px">
      <span class="bead b-blue" style="width:16px;height:16px"></span>
      <span class="bead b-green" style="width:20px;height:20px"></span>
      <span class="bead b-pink" style="width:18px;height:18px"></span>
    </div>
  </section>

  <section class="card front-bottom" aria-label="Card back">
    <div class="wordmark" style="left:70px;top:100px;color:#fff"><span class="dot" style="background:#fff"></span>Corvallina</div>
    <div class="wordmark-sub" style="left:300px;top:178px;color:#fff">GRETA MARLOW</div>
    <div class="rule" style="top:253px;height:3px"></div>
    <div class="beads" style="left:230px;top:244px">
      <span class="bead b-blue" style="width:18px;height:18px"></span>
      <span class="bead b-green" style="width:20px;height:20px"></span>
      <span class="bead b-grey" style="width:14px;height:14px"></span>
      <span class="bead b-pink" style="width:18px;height:18px"></span>
    </div>
  </section>

  <section class="card inside-bottom" aria-label="Card inside, lower panel">
    <div class="band band-taupe" style="top:0;height:58px"></div>
    <div class="beads" style="left:210px;top:44px">
      <span class="bead b-blue" style="width:28px;height:28px"></span>
      <span class="bead b-green" style="width:34px;height:34px"></span>
      <span class="bead b-pink" style="width:26px;height:26px"></span>
    </div>
    <address class="contact" style="top:162px;font-style:normal">
      27 Linden Hollow Road, Fairmont Vale, CA 90000<br>
      Email: greta@corvallina.com<br>
      www.corvallina.com
    </address>
    <div class="rule" style="top:246px;height:3px"></div>
    <div class="band band-magenta" style="top:249px;bottom:0"></div>
    <div class="beads" style="left:240px;top:236px">
      <span class="bead b-blue" style="width:18px;height:18px"></span>
      <span class="bead b-green" style="width:24px;height:24px"></span>
      <span class="bead b-pink" style="width:20px;height:20px"></span>
    </div>
  </section>

</main>
</body>
</html>
```